Food broker, trader, wholesaler, liquidator looking for a 5 pages website

Looking for a 5 pages website design. We are food brokers, traders, wholesaler and closeout buyer working with manufacturers, distributors, importers sell to retailers, food service operators and industrial (ingredients). We help market their products. We are a resource for those who need a solution in the distribution/selling/placement of food on the shelves, kitchens and pantries. Whether we open new accounts with new products or sell short dated inventory, we know where to go and get results.

Target Market(s)

Food manufacturers, food distributors, food brokers

Coding

Coded - Design and coding required

Number of Pages Required

4 page

Font styles to use
Serif

Requirements
Must have
• Food-food production-warehouse-Food packaging-people meeting-trucks-supermarket shelves-

```html
<!DOCTYPE html>
<html lang="en">
<head>
<meta charset="utf-8">
<title>Harborline Provisions</title>
<link rel="stylesheet" href="https://fonts.googleapis.com/css2?family=Alike&family=Noto+Serif:wght@400;700&family=Mulish:wght@400;600&display=swap">
<style>
:root{
  --navy:#101a6e;
  --navy-dark:#0c1459;
  --ink:#444a55;
  --muted:#6b6f78;
  --white:#ffffff;
  --line:#d9dbe0;
  --footer:#232323;
  --footer-text:#e8e8e8;
}
*{box-sizing:border-box;margin:0;padding:0}
html,body{width:1200px;height:3061px;overflow:hidden;background:var(--white)}
body{position:relative;font-family:"Noto Serif",serif;color:var(--ink)}
.abs{position:absolute}

/* header */
.site-header{position:absolute;left:0;top:0;width:1200px;height:115px;background:var(--white)}
.brand{position:absolute;left:110px;top:8px;width:175px;text-align:center}
.brand-mark{width:72px;height:72px;border-radius:50%;background:var(--navy);margin:0 auto}
.brand-name{font-family:"Noto Serif",serif;font-weight:700;font-size:12px;color:var(--navy);margin-top:12px;letter-spacing:.3px;white-space:nowrap}
.main-nav a{position:absolute;top:47px;font-family:"Noto Serif",serif;font-size:14px;color:#2d2f36;text-decoration:none}
.main-nav a.active{color:var(--navy)}

/* hero */
.hero{position:absolute;left:0;top:115px;width:1200px;height:606px;
  background:linear-gradient(180deg,#8fc4ee 0%,#b9dcf4 40%,#dcecf6 62%,#3b6c9c 72%,#284f7c 100%)}
.hero-title{position:absolute;left:686px;top:228px;font-family:"Alike",serif;font-size:49px;color:var(--navy);white-space:nowrap}
.hero-text{position:absolute;left:686px;top:302px;width:420px;font-size:17px;line-height:37px;color:#4a4f5a}
.btn-solid{position:absolute;background:var(--navy);color:var(--white);font-size:15px;display:flex;align-items:center;justify-content:center;border-radius:2px}
.slider-dots span{position:absolute;top:698px;width:10px;height:10px;border-radius:50%;background:var(--white)}
.slider-dots span.on{background:var(--navy)}

/* section headings */
.section-title{position:absolute;left:0;width:1200px;text-align:center;font-family:"Alike",serif;font-size:42px;color:var(--navy)}
.section-sub{position:absolute;left:0;width:1200px;text-align:center;font-size:15.5px;color:#4a4f5a}

/* process */
.process-line{position:absolute;left:166px;top:966px;width:866px;height:4px;background:var(--navy)}
.step{position:absolute;top:913px;width:110px;height:110px;border-radius:50%;border:2px solid var(--navy);background:var(--white);display:flex;align-items:center;justify-content:center}

/* about */
.about-panel{position:absolute;left:0;top:1107px;width:682px;height:484px;background:var(--navy)}
.about-photo{position:absolute;left:682px;top:1107px;width:518px;height:484px;background:linear-gradient(160deg,#dbe8f2 0%,#a9c6da 30%,#4f93b4 62%,#2a7aa0 100%)}
.about-title{position:absolute;left:139px;top:1178px;font-family:"Alike",serif;font-size:49px;color:var(--white)}
.about-rule{position:absolute;left:139px;top:1244px;width:60px;height:3px;background:var(--white)}
.about-text{position:absolute;left:139px;top:1276px;width:468px;font-size:12.5px;line-height:30px;color:var(--white);text-align:justify}
.btn-outline{position:absolute;left:139px;top:1483px;width:131px;height:48px;border:1px solid var(--white);color:var(--white);font-size:14px;display:flex;align-items:center;justify-content:center;border-radius:2px}

/* services */
.service-card{position:absolute;top:1755px;width:309px;height:390px;background:var(--white);box-shadow:0 0 5px rgba(0,0,0,.14)}
.service-photo{position:absolute;left:9px;top:9px;width:291px;height:215px}
.service-name{position:absolute;left:0;top:248px;width:100%;text-align:center;font-family:"Alike",serif;font-size:20px;color:#30343d}
.service-rule{position:absolute;left:133px;top:289px;width:42px;height:3px;background:var(--navy)}
.service-desc{position:absolute;left:30px;top:307px;width:249px;text-align:center;font-family:"Mulish",sans-serif;font-size:13px;line-height:25px;color:var(--muted)}

/* contact */
.contact{position:absolute;left:0;top:2206px;width:1200px;height:480px;background:linear-gradient(180deg,#eceef1 0%,#e6e8ea 100%)}
.field{position:absolute;background:var(--white);border:1px solid #cfd2d8;font-size:12.5px;color:#555a63;padding:13px 15px}

/* footer */
.site-footer{position:absolute;left:0;top:2686px;width:1200px;height:375px;background:var(--footer);color:var(--footer-text)}
.footer-brand{position:absolute;left:116px;top:99px;width:250px;text-align:center}
.footer-brand .brand-mark{width:134px;height:100px;border-radius:50%;background:var(--white)}
.footer-brand .brand-name{color:var(--white);font-size:16px;margin-top:16px}
.footer-head{position:absolute;top:44px;font-family:"Alike",serif;font-size:24px;color:var(--white)}
.footer-list{position:absolute;top:99px;list-style:none;font-family:"Mulish",sans-serif;font-size:14.5px}
.footer-list li{height:35px;display:flex;align-items:flex-start}
.footer-list li::before{content:"»";width:28px;font-size:14px}
.footer-note{position:absolute;left:836px;top:99px;width:260px;font-family:"Mulish",sans-serif;font-size:14.5px;line-height:25px}
.footer-input{position:absolute;left:836px;top:167px;width:250px;height:42px;background:var(--white);color:#444;font-family:"Mulish",sans-serif;font-size:14px;padding:12px 14px}
.footer-btn{position:absolute;left:836px;top:217px;width:96px;height:38px;background:var(--navy);color:var(--white);font-family:"Mulish",sans-serif;font-size:14px;display:flex;align-items:center;justify-content:center}
.footer-divider{position:absolute;left:114px;top:297px;width:972px;height:1px;background:#4a4a4a}
.copyright{position:absolute;left:0;top:327px;width:1200px;text-align:center;font-family:"Mulish",sans-serif;font-size:14px}
</style>
</head>
<body>

<header class="site-header">
  <div class="brand">
    <div class="brand-mark"></div>
    <div class="brand-name">HARBORLINE PROVISIONS</div>
  </div>
  <nav class="main-nav">
    <a class="active" style="left:583px">Home</a>
    <a style="left:671px">About Us</a>
    <a style="left:779px">What we do</a>
    <a style="left:906px">Contact</a>
    <a style="left:1006px">Giving Back</a>
  </nav>
</header>

<section class="hero" role="img" aria-label="Container ship and tugboat on open sea under a blue sky"></section>
<h1 class="hero-title">Harborline Provisions</h1>
<p class="hero-text">Sed ut perspiciatis unde omnis iste natus error sit voluptatem accusantium doloremque laudantium totam rem aperiam</p>
<div class="btn-solid" style="left:688px;top:425px;width:132px;height:50px">Read More</div>
<div class="slider-dots"><span style="left:576px"></span><span class="on" style="left:595px"></span><span style="left:613px"></span></div>

<h2 class="section-title" style="top:752px">Our Process</h2>
<p class="section-sub" style="top:822px">Sed ut perspiciatis unde omnis iste natus error sit voluptatem accusantium doloremque</p>

<div class="process-line"></div>
<div class="step" style="left:111px"><svg width="50" height="56" viewBox="0 0 50 56" fill="none" stroke="#101a6e" stroke-width="3" aria-label="Packaged goods"><rect x="12" y="4" width="26" height="10"/><rect x="5" y="14" width="40" height="38"/><line x1="5" y1="26" x2="45" y2="26"/><ellipse cx="25" cy="38" rx="11" ry="6"/></svg></div>
<div class="step" style="left:256px"><svg width="56" height="52" viewBox="0 0 56 52" fill="none" stroke="#101a6e" stroke-width="3" aria-label="Warehouse"><path d="M4 18 L28 4 L52 18 V48 H4 Z"/><rect x="16" y="26" width="24" height="22"/><rect x="24" y="36" width="10" height="12"/></svg></div>
<div class="step" style="left:400px"><svg width="58" height="50" viewBox="0 0 58 50" fill="none" stroke="#101a6e" stroke-width="3" aria-label="Meeting"><rect x="4" y="22" width="50" height="24" rx="4"/><line x1="20" y1="22" x2="20" y2="46"/><line x1="38" y1="22" x2="38" y2="46"/><circle cx="12" cy="12" r="0"/></svg></div>
<div class="step" style="left:544px"><svg width="52" height="54" viewBox="0 0 52 54" fill="none" stroke="#101a6e" stroke-width="3" aria-label="Production equipment"><rect x="4" y="6" width="44" height="30"/><rect x="28" y="12" width="14" height="14"/><line x1="10" y1="16" x2="22" y2="16"/><line x1="10" y1="24" x2="22" y2="24"/><line x1="26" y1="36" x2="26" y2="48"/><line x1="14" y1="48" x2="38" y2="48"/></svg></div>
<div class="step" style="left:689px"><svg width="62" height="46" viewBox="0 0 62 46" fill="none" stroke="#101a6e" stroke-width="3" aria-label="Delivery truck"><rect x="3" y="4" width="34" height="28"/><path d="M37 14 H50 L58 24 V32 H37"/><circle cx="14" cy="38" r="5"/><circle cx="47" cy="38" r="5"/></svg></div>
<div class="step" style="left:833px"><svg width="56" height="52" viewBox="0 0 56 52" fill="none" stroke="#101a6e" stroke-width="3" aria-label="Supermarket shelves"><rect x="4" y="4" width="48" height="44"/><line x1="4" y1="18" x2="52" y2="18"/><line x1="4" y1="33" x2="52" y2="33"/><rect x="10" y="8" width="8" height="10"/><rect x="24" y="22" width="10" height="11"/><rect x="38" y="37" width="8" height="11"/></svg></div>
<div class="step" style="left:977px"><svg width="60" height="52" viewBox="0 0 60 52" fill="none" stroke="#101a6e" stroke-width="3" aria-label="Hot dish"><path d="M6 28 H54 C54 40 44 46 30 46 C16 46 6 40 6 28 Z"/><path d="M20 18 C18 12 22 10 20 4"/><path d="M30 18 C28 12 32 10 30 4"/><path d="M40 18 C38 12 42 10 40 4"/></svg></div>

<section class="about-panel"></section>
<div class="about-photo" role="img" aria-label="Loaded container ship leaving a city port"></div>
<h2 class="about-title">About Us</h2>
<div class="about-rule"></div>
<p class="about-text">Harborline Provisions works with food manufacturers, brand owners, distributors and wholesalers market their products. Retail, Food Service and Industrial ingredients.Founded in 2008, Harborline Provisions started with the distribution of gluten free products understanding the need to provide access to unique flavors and products forthe celiac consumers. From this, we expanded into deli, dairy, groceries, frozen and beverages.</p>
<div class="btn-outline">READ MORE</div>

<h2 class="section-title" style="top:1632px">What We Do</h2>
<p class="section-sub" style="top:1694px">Sed ut perspiciatis unde omnis iste natus error sit voluptatem accusantium doloremque</p>

<article class="service-card" style="left:112px">
  <div class="service-photo" role="img" aria-label="Sales team meeting in front of a chart display" style="background:linear-gradient(135deg,#2b3342 0%,#5c6676 50%,#c9d2d6 100%)"></div>
  <h3 class="service-name">Sales &amp; Marketing</h3>
  <div class="service-rule"></div>
  <p class="service-desc">we connect food buyers and sellers through a dedicated approach.</p>
</article>
<article class="service-card" style="left:445px">
  <div class="service-photo" role="img" aria-label="Trader typing on a laptop beside market screens" style="background:linear-gradient(135deg,#1f2b3d 0%,#44546b 45%,#b79878 100%)"></div>
  <h3 class="service-name">Trading</h3>
  <div class="service-rule"></div>
  <p class="service-desc">we purchase goods anywhere and ship them Nationwide and Export.</p>
</article>
<article class="service-card" style="left:779px">
  <div class="service-photo" role="img" aria-label="Warehouse aisle with pallets and a forklift" style="background:linear-gradient(180deg,#b9c6d6 0%,#c79a6b 50%,#9aa3ab 100%)"></div>
  <h3 class="service-name">Closeout/Excess Inventory</h3>
  <div class="service-rule"></div>
  <p class="service-desc">we buy closeouts and excess inventory for prisons, outlet stores and discounters.</p>
</article>

<section class="contact" role="img" aria-label="Faded warehouse interior background"></section>
<h2 class="section-title" style="top:2253px">Contact Us</h2>
<p class="section-sub" style="top:2314px">Sed ut perspiciatis unde omnis iste natus error sit voluptatem accusantium</p>
<div class="field" style="left:280px;top:2367px;width:315px;height:45px">First Name :</div>
<div class="field" style="left:606px;top:2367px;width:314px;height:45px">Last Name :</div>
<div class="field" style="left:280px;top:2422px;width:315px;height:45px">Email :</div>
<div class="field" style="left:606px;top:2422px;width:314px;height:45px">Phone :</div>
<div class="field" style="left:280px;top:2477px;width:640px;height:89px">Message :</div>
<div class="btn-solid" style="left:526px;top:2588px;width:148px;height:48px;font-size:14px">SUBMIT</div>

<footer class="site-footer">
  <div class="footer-brand">
    <div class="brand-mark" style="margin:0 auto"></div>
    <div class="brand-name">HARBORLINE PROVISIONS</div>
  </div>
  <h4 class="footer-head" style="left:396px">Quick Links</h4>
  <ul class="footer-list" style="left:396px">
    <li>Home</li><li>About Us</li><li>What we do</li><li>Contact</li><li>Giving Back</li>
  </ul>
  <h4 class="footer-head" style="left:613px">Services</h4>
  <ul class="footer-list" style="left:613px">
    <li>Sed ut perspiciatis</li><li>unde omnis iste</li><li>natus error sit</li><li>voluptatem</li><li>accusantium</li>
  </ul>
  <h4 class="footer-head" style="left:836px">Newsletter</h4>
  <p class="footer-note">Sed ut perspiciatis unde omnis iste natus error sit voluptatem</p>
  <div class="footer-input">Email :</div>
  <div class="footer-btn">SUBMIT</div>
  <div class="footer-divider"></div>
  <p class="copyright">© Copyright 2020 Harborline Provisions.All Rights Reserved</p>
</footer>

</body>
</html>
```